Souvenir and Health Food Products

We need a website designed for a Wholesaler & Distributor of Australia Made Souvenir & Health Food products. Our range includes many of Australia's leading brands: Meadow's Porch, Coastal from Gumtrail, Pebble & Fernly, Vira Cosmetics, Dalquen, T R Leathergoods, Presholt Leathergoods, Wendrick's Salt & Gladmoor Honey.

Design will be converted into a Dot Net Nuke skin and containers so needs to be compatible.

Needs to show off their products and be easy to navigate.

Would like a nice clean and corporate look.

Hi Everyone

All design concepts are with my client who has been extremely busy....hoping to get feedback from them this week.

Cheers
Tamsin

Target Market(s)

Target market are retail shops looking to stock their products

Industry/Entity Type

Health

Number of Pages Required

2 pages

Requirements
Must have
• Proposed Site Map
• Home
• About Us
• Products
• Ordering
• Contact Us

• To be included in homepage design concept:

• Large area for a flash banner of rotating images on homepage
• Logo and Phone number in header for every page 07 5519 3027
• Some welcome text
• Some icons will need to be designed - Register for our newsletter and Contact Us
• Product category list on homepage – thumbnail image/name of category (click through)

• Product categories to use are:
• (allow for up to 15)
• • Meadow’s Porch (use p1000321/jpg)

• • Jojoba Oil (use TFP_0121.jpg))

• • Coastal from Gumtrail (use TFP_0077.jpg)

• Could you create a separate content page to show how products will look on category page with each product having a thumbnail image, description and Enquire now button.
Should not have
• No shopping cart or ecommerce needed

```html
<!DOCTYPE html>
<html lang="en">
<head>
<meta charset="utf-8">
<title>Korrin International – Website Concept</title>
<link href="https://fonts.googleapis.com/css2?family=Arimo:wght@400;700&display=swap" rel="stylesheet">
<style>
:root{
  --bg-a:#8b8b8b;
  --bg-b:#979797;
  --white:#ffffff;
  --blue:#1aa0d8;
  --blue-dark:#0f7fc4;
  --blue-light:#5cc3ef;
  --heading:#1697c9;
  --text:#1c1c1c;
  --panel:#d9d9d9;
  --panel-row:#e4e4e4;
  --panel-row-alt:#d6d6d6;
  --grey-btn:#6f6f6f;
}
*{box-sizing:border-box;margin:0;padding:0}
html,body{width:1200px;height:2422px;overflow:hidden}
body{
  font-family:"Arimo",Arial,sans-serif;
  color:var(--text);
  background:repeating-linear-gradient(to bottom,var(--bg-a) 0 4px,var(--bg-b) 4px 8px);
  position:relative;
}
.page{position:absolute;left:0;width:1200px;height:1137px}
.page--home{top:0}
.page--product{top:1211px}
.sheet{position:absolute;left:78px;top:0;width:1047px;height:1090px;background:var(--white);box-shadow:0 0 6px rgba(0,0,0,.35)}
.banner{position:absolute;left:86px;top:0;width:1029px;height:218px;background:linear-gradient(90deg,#5d9be0 0%,#8cc5ef 40%,#e8f3fb 85%,#fff 100%)}
.banner__photo{position:absolute;left:0;top:0;width:596px;height:218px;background:linear-gradient(135deg,#8aa43a 0%,#b7c24a 35%,#6d7d2a 60%,#c9b14a 80%,#9fb43e 100%)}
.brand{position:absolute;left:98px;top:246px;display:flex;align-items:center;gap:10px}
.brand__mark{width:34px;height:34px;border-radius:50%;background:var(--blue)}
.brand__name{font-size:27px;font-weight:700;color:#1b1b1b;letter-spacing:.5px}
.brand__phone{position:absolute;left:181px;top:298px;font-size:19px;color:var(--blue)}
.nav{position:absolute;left:427px;top:229px;height:44px;display:flex;border-radius:5px;overflow:hidden;background:linear-gradient(#5cc7f3,#1a9fe0)}
.nav a{display:flex;align-items:center;justify-content:center;color:#fff;font-weight:700;font-size:17px;text-decoration:none;border-right:2px solid #e9f6fd;height:44px}
.nav a:last-child{border-right:0}
.tile{position:absolute;top:360px;width:158px;height:133px;border-radius:5px;background:linear-gradient(#6fcff6,#1aa2e0);color:#fff;text-align:center;font-size:19px;line-height:19px;border:2px solid #9fdcf6}
.tile svg{display:block;margin:12px auto 8px}
.tile--news{left:88px}
.tile--contact{left:257px}
.categories{position:absolute;left:88px;top:504px;width:328px;height:536px;background:var(--panel);border-radius:4px;padding:6px}
.categories h2{font-size:25px;font-weight:400;color:#111;padding:8px 8px 7px;background:#eee}
.categories ul{list-style:none}
.categories li{height:39px;display:flex;align-items:center;font-size:19px;padding-left:8px;background:var(--panel-row)}
.categories li:nth-child(even){background:var(--panel-row-alt)}
.categories li::before{content:"";border-left:11px solid #9a9a9a;border-top:8px solid transparent;border-bottom:8px solid transparent;margin-right:9px}
.content{position:absolute;left:469px;top:0;width:600px}
.title{position:absolute;top:311px;font-size:31px;font-weight:700;color:var(--heading);white-space:nowrap}
.copy{position:absolute;font-size:14px;line-height:18.5px;width:568px}
.featured-title{position:absolute;top:514px;font-size:31px;font-weight:700;color:var(--heading)}
.product{position:absolute;width:220px;text-align:center;font-size:19px}
.product__img{display:block;width:120px;height:105px;margin:0 auto 12px;border-radius:4px}
.img-herbal{background:linear-gradient(135deg,#c9c7a8 0%,#6f8a3a 55%,#a2b07a 100%)}
.img-jojoba{background:linear-gradient(135deg,#d2233e 0%,#c81c36 45%,#f2b316 70%,#f6d34a 100%)}
.img-jars{background:linear-gradient(135deg,#2f6a4c 0%,#e9eae3 45%,#3e7b55 70%,#5b4b3c 100%)}
.hero-img{position:absolute;left:55px;top:349px;width:458px;height:436px;border-radius:6px;background:linear-gradient(135deg,#c51b34 0%,#d92b43 40%,#f5ba18 65%,#f8d848 100%)}
.enquire{position:absolute;left:0;top:951px;width:88px;height:43px;border-radius:5px;background:linear-gradient(#9a9a9a,var(--grey-btn));color:#fff;font-size:17px;display:flex;align-items:center;justify-content:center;border:1px solid #555}
.footer{position:absolute;left:74px;top:1088px;width:1054px;height:49px;background:linear-gradient(#2fa9ea,var(--blue-dark));border-radius:0 0 6px 6px;border-top:3px solid #0d5f94;color:#fff;font-size:17px;text-align:right;padding:14px 16px 0 0;box-shadow:0 2px 4px rgba(0,0,0,.3)}
</style>
</head>
<body>

<section class="page page--home">
  <div class="sheet"></div>
  <div class="banner"><div class="banner__photo" role="img" aria-label="Rotating banner photo of eucalyptus soap and eucalyptus oil products on leaves"></div></div>
  <div class="brand"><span class="brand__mark"></span><span class="brand__name">Korrin International</span></div>
  <div class="brand__phone">Call us at 07 5519 3027</div>
  <nav class="nav"><a style="width:120px">Home</a><a style="width:137px">About Us</a><a style="width:136px">Products</a><a style="width:133px">Ordering</a><a style="width:161px">Contact Us</a></nav>
  <div class="tile tile--news"><svg width="40" height="52" viewBox="0 0 40 52"><rect x="2" y="2" width="36" height="48" fill="#f4f4f4" stroke="#555" stroke-width="2"/><g stroke="#444" stroke-width="3"><line x1="9" y1="13" x2="31" y2="13"/><line x1="9" y1="21" x2="31" y2="21"/><line x1="9" y1="29" x2="31" y2="29"/><line x1="9" y1="37" x2="31" y2="37"/></g></svg>Sign up for our<br>free newsletter</div>
  <div class="tile tile--contact"><svg width="54" height="36" viewBox="0 0 54 36" style="margin-top:20px;margin-bottom:12px"><rect x="2" y="2" width="50" height="32" fill="#f4f4f4" stroke="#555" stroke-width="2"/><path d="M2 2 L27 22 L52 2 M2 34 L21 17 M52 34 L33 17" fill="none" stroke="#555" stroke-width="2"/></svg>Contact<br>Us</div>
  <aside class="categories"><h2>Our Product Categories</h2><ul><li>Health Food</li><li>Vitamins &amp; Supplements</li><li>Soaps &amp; Scents</li><li>Food Seasonings</li><li>Cleaning Products</li><li>Souvenirs</li><li>Australian Hand Made</li><li>Organic Foods</li><li>Gift Baskets</li><li>Flavor Enhancers</li><li>Diet Solutions</li><li>Soup Mixes</li></ul></aside>
  <main class="content">
    <h1 class="title">Welcome to Korrin International.</h1>
    <p class="copy" style="top:362px">Lorem ipsum dolor sit amet, consectetur adipiscing elit. Proin sed dui at metus<br>sodales eleifend quis at ligula. Fusce interdum massa ac sem viverra luctus. Nam ut<br>urna orci. Sed malesuada blandit est, id vehicula arcu gravida consectetur.</p>
    <p class="copy" style="top:435px">Etiam ultricies lacus non erat pellentesque ut sagittis nunc faucibus. In quis neque<br>arcu. Pellentesque habitant morbi tristique senectus et netus et malesuada.<br>viverra luctus. Nam ut urna orci. Sed malesuada blandit est, id vehicula.</p>
    <h2 class="featured-title">Featured Products</h2>
    <div class="product" style="left:-38px;top:567px"><span class="product__img img-herbal" role="img" aria-label="Herbal tea and soap products"></span>Meadow’s Porch</div>
    <div class="product" style="left:191px;top:567px"><span class="product__img img-jojoba" role="img" aria-label="Jojoba oil bottles and boxes"></span>Jojoba Oil</div>
    <div class="product" style="left:420px;top:567px"><span class="product__img img-jars" role="img" aria-label="Assorted skincare jars"></span>Coastal from Gumtrail</div>
    <div class="product" style="left:-38px;top:725px"><span class="product__img img-jojoba" role="img" aria-label="Jojoba oil bottles and boxes"></span>Jojoba Oil</div>
    <div class="product" style="left:191px;top:725px"><span class="product__img img-jars" role="img" aria-label="Assorted skincare jars"></span>Coastal from Gumtrail</div>
    <div class="product" style="left:420px;top:725px"><span class="product__img img-herbal" role="img" aria-label="Herbal tea and soap products"></span>Meadow’s Porch</div>
    <div class="product" style="left:-38px;top:884px"><span class="product__img img-jars" role="img" aria-label="Assorted skincare jars"></span>Coastal from Gumtrail</div>
    <div class="product" style="left:191px;top:884px"><span class="product__img img-herbal" role="img" aria-label="Herbal tea and soap products"></span>Meadow’s Porch</div>
    <div class="product" style="left:420px;top:884px"><span class="product__img img-jojoba" role="img" aria-label="Jojoba oil bottles and boxes"></span>Jojoba Oil</div>
  </main>
  <footer class="footer">©Korrin International 2009</footer>
</section>

<section class="page page--product">
  <div class="sheet"></div>
  <div class="banner"><div class="banner__photo" role="img" aria-label="Rotating banner photo of eucalyptus soap and eucalyptus oil products on leaves"></div></div>
  <div class="brand"><span class="brand__mark"></span><span class="brand__name">Korrin International</span></div>
  <div class="brand__phone">Call us at 07 5519 3027</div>
  <nav class="nav"><a style="width:120px">Home</a><a style="width:137px">About Us</a><a style="width:136px">Products</a><a style="width:133px">Ordering</a><a style="width:161px">Contact Us</a></nav>
  <div class="tile tile--news"><svg width="40" height="52" viewBox="0 0 40 52"><rect x="2" y="2" width="36" height="48" fill="#f4f4f4" stroke="#555" stroke-width="2"/><g stroke="#444" stroke-width="3"><line x1="9" y1="13" x2="31" y2="13"/><line x1="9" y1="21" x2="31" y2="21"/><line x1="9" y1="29" x2="31" y2="29"/><line x1="9" y1="37" x2="31" y2="37"/></g></svg>Sign up for our<br>free newsletter</div>
  <div class="tile tile--contact"><svg width="54" height="36" viewBox="0 0 54 36" style="margin-top:20px;margin-bottom:12px"><rect x="2" y="2" width="50" height="32" fill="#f4f4f4" stroke="#555" stroke-width="2"/><path d="M2 2 L27 22 L52 2 M2 34 L21 17 M52 34 L33 17" fill="none" stroke="#555" stroke-width="2"/></svg>Contact<br>Us</div>
  <aside class="categories"><h2>Our Product Categories</h2><ul><li>Health Food</li><li>Vitamins &amp; Supplements</li><li>Soaps &amp; Scents</li><li>Food Seasonings</li><li>Cleaning Products</li><li>Souvenirs</li><li>Australian Hand Made</li><li>Organic Foods</li><li>Gift Baskets</li><li>Flavor Enhancers</li><li>Diet Solutions</li><li>Soup Mixes</li></ul></aside>
  <main class="content">
    <h1 class="title">Jojoba Oil</h1>
    <div class="hero-img" role="img" aria-label="Jojoba oil bottles with red gift boxes"></div>
    <p class="copy" style="top:813px">Lorem ipsum dolor sit amet, consectetur adipiscing elit. Proin sed dui at metus<br>sodales eleifend quis at ligula. Fusce interdum massa ac sem viverra luctus. Nam ut<br>urna orci. Sed malesuada blandit est, id vehicula arcu gravida consectetur.</p>
    <p class="copy" style="top:886px">Etiam ultricies lacus non erat pellentesque ut sagittis nunc faucibus. In quis neque<br>arcu. Pellentesque habitant morbi tristique senectus et netus et malesuada.<br>viverra luctus. Nam ut urna orci. Sed malesuada blandit est, id vehicula.</p>
    <a class="enquire">Enquire</a>
  </main>
  <footer class="footer">©Korrin International 2009</footer>
</section>

</body>
</html>
```